Catalogue Design Project - Cosmetic

We are a new Toronto based company looking to make a cosmetics catalogue. Our company is Brindle Wholesale which is short for Brindle Pemwick Supply Wholesale. We need a stylish but simple catalogue that looks classy. Please keep front and back cover black.

The use of modern typefaces and an element of consistency across the catalogue is also important. Stock images have been provided. Please do not use the stock images as collages, crop and use only 1 picture at a time.

This will be roughly a 24 page catalogue and everything will be outlined to make it easy. Most of the products we will be carrying can be seen at http://glossvarnelle.com/.

Page size is 8.5 x 11inch

We have provided a template to show where everything should go, this should not be used for design purposes. Just look for the Brindle Wholesale Template files. All photos are provided, there are doubles of pictures and they do not have to be used.

Please have a look at http://www.quivelbeauty.ca/. That is the look we are going for.
Updates

Target Market(s)

Small to medium-sized businesses looking to carry this product in their outlets.

Industry/Entity Type

Cosmetics

Requirements
Must have
• Use of Brindle Wholesale logo (provided)
Table of Contents
Page Numbers
Product photos (provided)
Follow general page order of provided template
All text/content (text for catalog doc)

Will require source files after project is complete.

```html
<!DOCTYPE html>
<html lang="en">
<head>
<meta charset="utf-8">
<title>Brindle Wholesale Catalog Cover</title>
<link rel="stylesheet" href="https://fonts.googleapis.com/css2?family=Source+Sans+3:wght@400;600&display=swap">
<style>
  :root {
    --backdrop: #e6dfcc;
    --cover-black: #000000;
    --frame-plum: #2a1d20;
    --plate-dark: #28231f;
    --plate-edge: #8e8e8e;
    --text-white: #ffffff;
    --text-grey: #7c7c7c;
    --tagline-grey: #c9c4c4;
    --dot-1: #ffffff;
    --dot-2: #e6e6e6;
    --dot-3: #c8c8c8;
    --dot-4: #8c8c8c;
    --dot-5: #666666;
    --dot-6: #444444;
    --dot-7: #262626;
  }
  * { margin: 0; padding: 0; box-sizing: border-box; }
  html, body {
    width: 1200px; height: 771px; overflow: hidden;
    background: var(--backdrop);
    font-family: "Source Sans 3", "Myriad Pro", sans-serif;
  }
  .canvas { position: relative; width: 1200px; height: 771px; }
  .spread {
    position: absolute; left: 91px; top: 59px;
    width: 1015px; height: 657px;
    background: var(--cover-black);
  }
  /* back cover */
  .back-cover__site {
    position: absolute; left: 0; top: 326px; width: 490px;
    text-align: center; color: var(--text-grey);
    font-size: 23px; letter-spacing: 3px;
  }
  .back-cover__contact {
    position: absolute; left: 0; top: 552px; width: 490px;
    text-align: center; color: var(--text-white);
  }
  .back-cover__phone { font-size: 16px; letter-spacing: 0.3px; }
  .back-cover__web { font-size: 10px; letter-spacing: 2px; margin-top: 2px; }
  .dot-row { display: flex; justify-content: center; gap: 6px; }
  .dot-row span { width: 9px; height: 9px; border-radius: 50%; }
  .dot-row span:nth-child(1) { background: var(--dot-1); }
  .dot-row span:nth-child(2) { background: var(--dot-2); }
  .dot-row span:nth-child(3) { background: var(--dot-3); }
  .dot-row span:nth-child(4) { background: var(--dot-4); }
  .dot-row span:nth-child(5) { background: var(--dot-5); }
  .dot-row span:nth-child(6) { background: var(--dot-6); }
  .dot-row span:nth-child(7) { background: var(--dot-7); }
  .back-cover__contact .dot-row { margin-top: 8px; }
  /* front cover */
  .front-cover__frame {
    position: absolute; left: 517px; top: 38px;
    width: 492px; height: 571px;
    background: var(--frame-plum);
  }
  .front-cover__photo {
    position: absolute; left: 517px; top: 55px;
    width: 472px; height: 554px;
    background: linear-gradient(100deg, #c9a48f 0%, #a57e6c 30%, #4a3a36 55%, #2b2524 75%, #5d5a58 100%);
  }
  .logo-plate {
    position: absolute; left: 734px; top: 266px;
    width: 272px; height: 89px;
    background: var(--plate-dark);
  }
  .logo-plate::after {
    content: ""; position: absolute; right: -8px; top: 0;
    width: 8px; height: 89px; background: var(--plate-edge);
  }
  .logo-plate__name {
    position: absolute; left: 12px; top: 22px;
    color: var(--text-white); font-size: 20px; letter-spacing: 2.2px;
  }
  .logo-plate__tagline {
    position: absolute; left: 13px; top: 56px;
    color: var(--tagline-grey); font-size: 9.5px; letter-spacing: 0.6px;
  }
  .front-cover__label {
    position: absolute; left: 517px; top: 614px; width: 492px;
    text-align: center; color: var(--text-white);
    font-size: 12px; letter-spacing: 5px;
  }
  .front-cover__label .dot-row { margin-top: 5px; }
</style>
</head>
<body>
<div class="canvas">
  <div class="spread">
    <section class="back-cover">
      <p class="back-cover__site">BRINDLEWHOLESALE.CA</p>
      <div class="back-cover__contact">
        <p class="back-cover__phone">987-654-3210</p>
        <p class="back-cover__web">www.website.com</p>
        <div class="dot-row"><span></span><span></span><span></span><span></span><span></span><span></span><span></span></div>
      </div>
    </section>
    <section class="front-cover">
      <div class="front-cover__frame"></div>
      <div class="front-cover__photo" role="img" aria-label="Beauty portrait of a model with dark flowing hair, hands raised to her face"></div>
      <div class="logo-plate">
        <p class="logo-plate__name">BRINDLEWHOLESALE.CA</p>
        <p class="logo-plate__tagline">TORONTO'S QUALITY COSMETIC WHOLESALERS</p>
      </div>
      <div class="front-cover__label">
        <p>CATALOG</p>
        <div class="dot-row"><span></span><span></span><span></span><span></span><span></span><span></span><span></span></div>
      </div>
    </section>
  </div>
</div>
</body>
</html>
```